Consulting Firm stationery design

Now that the MakerHive has given us a new logo we'll now need to have all our stationery designed. So we're asking for this community to help us once again.We're looking to get from you Letterheads (Header and Footer, suitable to be applied on a .docx format. Vectors are required but keep this in mind), Envelopes (Front and Back designs, back is not a must but desirable depending on your design), 9"x 12" Pocket Folders (consider design for front and back, also for pockets as well), Business Cards.An elegant design is a must have, mostly for Folders and Envelopes. The idea with this two is to stand out from others when they're handed over. Ideas are welcomed, we were thinking maybe on some texturing simulation for these.Folders will have 3 addresses and contact information. Envelopes will have 1 address and contact information.Brand Manual attached. vendaluxo logo has been copyrighted already. I'm also attaching the current stationary designs (these never got to be out for production but was going to be before we made the brand changes); Pocker folders page 1 to 4 (pages 2 and 4 are the pocket designs), Pages 5 and 6 (6 is the back of the envelope), Pages 7 and 8 (8 is the back of the business card). No letterhead within these designs as it just had the logo and address.

Industry/Entity Type

Business Consultant

Font styles to use
Serif
Sans Serif

Requirements
Must have
• Elegance
Nice to have
• Modern looking out of common

```html
<!DOCTYPE html>
<html lang="en">
<head>
<meta charset="utf-8">
<title>vendaluxo — Pocket Folder, Back and Front</title>
<link rel="stylesheet" href="https://fonts.googleapis.com/css2?family=Montserrat:wght@400;600;700&display=swap">
<style>
  :root {
    --stage: #e4e4e6;
    --brand-blue: #0280c0;
    --brand-blue-deep: #026ea6;
    --ink-black: #232326;
    --ink-black-deep: #141416;
    --mark-light: #d9d9db;
    --mark-grey: #6f7075;
    --accent-blue: #0a84c6;
    --white: #ffffff;
  }
  * { margin: 0; padding: 0; box-sizing: border-box; }
  html, body {
    width: 1200px;
    height: 1200px;
    overflow: hidden;
    background: var(--stage);
    font-family: "Montserrat", sans-serif;
  }
  .folder-spread {
    position: absolute;
    left: 60px;
    top: 240px;
    width: 1080px;
    height: 720px;
    display: flex;
    box-shadow: 0 18px 40px rgba(0,0,0,0.22);
  }
  .panel {
    position: relative;
    width: 540px;
    height: 720px;
    overflow: hidden;
  }
  .panel--back {
    background: linear-gradient(100deg, var(--brand-blue) 0%, var(--brand-blue-deep) 100%);
  }
  .panel--front {
    background: linear-gradient(100deg, var(--ink-black) 0%, var(--ink-black-deep) 100%);
  }
  .wordmark {
    position: absolute;
    left: 0;
    right: 0;
    display: flex;
    align-items: center;
    justify-content: center;
    gap: 12px;
    font-weight: 700;
    font-size: 64px;
    letter-spacing: -1px;
    line-height: 1;
  }
  .panel--back .wordmark { top: 318px; color: var(--mark-light); }
  .panel--front .wordmark { top: 250px; color: var(--mark-grey); }
  .wordmark__dot {
    width: 18px;
    height: 18px;
    border-radius: 50%;
    flex: none;
    margin-top: -38px;
  }
  .panel--back .wordmark__dot { background: var(--mark-light); }
  .panel--front .wordmark__dot { background: var(--accent-blue); }
  .contact-block {
    position: absolute;
    left: 56px;
    bottom: 58px;
    color: var(--white);
    font-size: 11px;
    line-height: 1.45;
  }
  .contact-block__office { font-weight: 700; }
  .contact-block__address { font-weight: 400; opacity: 0.92; margin-bottom: 12px; }
  .contact-line {
    display: flex;
    align-items: center;
    gap: 8px;
    font-weight: 600;
  }
  .contact-line svg { width: 10px; height: 10px; flex: none; }
</style>
</head>
<body>
  <main class="folder-spread">
    <section class="panel panel--back" aria-label="Folder back cover">
      <div class="wordmark">vendaluxo<span class="wordmark__dot"></span></div>
      <address class="contact-block" style="font-style: normal;">
        <div class="contact-block__office">Global Sales</div>
        <div class="contact-block__address">
          418 Harbor Crest Avenue, Suite C4<br>
          Dover, Delaware 19901<br>
          United States
        </div>
        <div class="contact-line">
          <svg viewBox="0 0 10 10" aria-hidden="true"><path d="M2 1 L4 1 L4.6 3.2 L3.4 4 Q4.4 5.8 6 6.6 L6.8 5.4 L9 6 L9 8 Q5 9.5 1 3 Z" fill="#fff"/></svg>
          +1 (555) 302-4178
        </div>
        <div class="contact-line">
          <svg viewBox="0 0 10 10" aria-hidden="true"><rect x="0.8" y="2" width="8.4" height="6" fill="none" stroke="#fff" stroke-width="1"/><path d="M0.8 2 L5 5.4 L9.2 2" fill="none" stroke="#fff" stroke-width="1"/></svg>
          info@vendaluxo.do
        </div>
        <div class="contact-line">
          <svg viewBox="0 0 10 10" aria-hidden="true"><circle cx="5" cy="5" r="4" fill="none" stroke="#fff" stroke-width="0.9"/><ellipse cx="5" cy="5" rx="1.8" ry="4" fill="none" stroke="#fff" stroke-width="0.8"/><line x1="1" y1="5" x2="9" y2="5" stroke="#fff" stroke-width="0.8"/></svg>
          www.vendaluxo.do
        </div>
      </address>
    </section>
    <section class="panel panel--front" aria-label="Folder front cover">
      <div class="wordmark">vendaluxo<span class="wordmark__dot"></span></div>
    </section>
  </main>
</body>
</html>
```